M Website

We need a website design for a construction plant company. You may use a combination of our photos and the stock images. See the logo for company colours. It also be of great value to see moving pictures like the ones on the link: https://www.quindellworks.co.za/copy-of-about-us. See our uploaded files for content.

Target Market(s)

Construction

Number of Pages Required

5+ page

```html
<!DOCTYPE html>
<html lang="en">
<head>
<meta charset="utf-8">
<title>Main Principles</title>
<link href="https://fonts.googleapis.com/css2?family=Roboto:wght@300;400;500&family=Roboto+Condensed:wght@700&display=swap" rel="stylesheet">
<style>
:root{
  --gold:#f2b705;
  --ink:#1c1c1c;
  --text:#2a2a2a;
  --band:#1d1d1d;
  --footer:#0a0a0a;
  --footer-text:#cfcfcf;
  --faint:#fafafa;
  --badge-blue:#2a3a8c;
  --badge-red:#c0202a;
  --badge-sky:#1a9ad6;
}
*{box-sizing:border-box;margin:0;padding:0}
html,body{width:968px;height:1200px;overflow:hidden;background:#fff}
body{position:relative;font-family:"Roboto",sans-serif;color:var(--text)}
.abs{position:absolute}
.section-title{position:absolute;font-family:"Roboto Condensed",sans-serif;font-weight:700;font-size:24px;color:var(--ink);letter-spacing:.2px;padding:6px 10px;white-space:nowrap}
.section-title::before,.section-title::after{content:"";position:absolute;width:9px;height:9px;border:0 solid var(--gold)}
.section-title::before{left:0;top:0;border-top-width:2px;border-left-width:2px}
.section-title::after{right:0;bottom:0;border-bottom-width:2px;border-right-width:2px}
.pattern{position:absolute;background:var(--faint)}
.card{position:absolute;left:50px;top:122px;width:258px;height:228px;background:#fff;box-shadow:0 6px 22px rgba(0,0,0,.13)}
.corner{position:absolute;width:19px;height:19px;border:0 solid var(--gold)}
.corner.tl{left:32px;top:104px;border-top-width:3px;border-left-width:3px}
.corner.br{left:309px;top:350px;border-bottom-width:3px;border-right-width:3px}
.principle-name{position:absolute;font-size:12px;font-weight:500;letter-spacing:3px;color:var(--ink);white-space:nowrap;text-align:right}
.bracket{color:var(--gold);font-weight:400;letter-spacing:0}
.principle-text{position:absolute;font-size:12.5px;line-height:20px;letter-spacing:.3px;text-align:right;white-space:nowrap;color:var(--text)}
.icon{position:absolute}
.band{position:absolute;left:0;top:818px;width:389px;height:103px;background:var(--band);color:#fff}
.band p{position:absolute;right:26px;font-size:12px;font-weight:500;letter-spacing:2.6px;text-align:right;white-space:nowrap}
.footer{position:absolute;left:0;top:1010px;width:968px;height:190px;background:var(--footer)}
.footer h3{position:absolute;top:32px;font-size:12.5px;font-weight:500;letter-spacing:3px;color:#fff;white-space:nowrap}
.footer address{position:absolute;top:74px;font-style:normal;font-size:12.5px;font-weight:300;line-height:23px;color:var(--footer-text);white-space:nowrap}
.contact-row{display:flex;align-items:center;gap:10px}
</style>
</head>
<body>

<div class="pattern" role="img" aria-label="Faint grid of small plus marks" style="left:672px;top:14px;width:258px;height:130px"></div>
<div class="pattern" role="img" aria-label="Faint grid of small plus marks" style="left:74px;top:624px;width:262px;height:180px"></div>
<div class="pattern" role="img" aria-label="Faint grid of small plus marks" style="left:74px;top:926px;width:262px;height:72px"></div>

<h2 class="section-title" style="left:382px;top:24px">MAIN PRINCIPLES</h2>

<div class="corner tl"></div>
<div class="card"></div>
<div class="corner br"></div>

<svg class="icon" style="left:72px;top:150px" width="58" height="58" viewBox="0 0 58 58" fill="none" stroke="var(--gold)" stroke-width="2">
  <circle cx="29" cy="29" r="27" stroke-dasharray="4 2"/><circle cx="29" cy="29" r="21"/>
  <path d="M19 27h6v12h-6zM25 28l5-8c2 0 3 1 3 3l-1 4h7c2 0 3 2 2 3l-2 8c-1 2-2 2-3 2H25"/>
</svg>
<svg class="icon" style="left:378px;top:148px" width="50" height="58" viewBox="0 0 50 58" fill="none" stroke="var(--gold)" stroke-width="2">
  <rect x="2" y="5" width="32" height="44" rx="2"/><rect x="11" y="1" width="14" height="7" rx="2"/>
  <path d="M8 18h8M8 26h8M20 18h8M20 24h8M8 34h20M8 40h16"/>
  <circle cx="38" cy="46" r="9" fill="#fff"/><path d="M34 46l3 3 6-6"/>
</svg>
<svg class="icon" style="left:686px;top:152px" width="40" height="48" viewBox="0 0 40 48" fill="none" stroke="var(--gold)" stroke-width="2">
  <path d="M20 2l17 6v14c0 12-8 20-17 24C11 42 3 34 3 22V8z"/><path d="M20 7l12 4v11c0 9-6 15-12 18-6-3-12-9-12-18V11z"/>
  <circle cx="20" cy="22" r="7"/><path d="M17 22l2 2 4-4"/>
</svg>

<svg class="icon" style="left:72px;top:431px" width="58" height="58" viewBox="0 0 58 58" fill="none" stroke="var(--gold)" stroke-width="2">
  <circle cx="29" cy="29" r="27" stroke-dasharray="4 2"/><circle cx="29" cy="29" r="21"/>
  <path d="M19 27h6v12h-6zM25 28l5-8c2 0 3 1 3 3l-1 4h7c2 0 3 2 2 3l-2 8c-1 2-2 2-3 2H25"/>
</svg>
<svg class="icon" style="left:378px;top:429px" width="50" height="58" viewBox="0 0 50 58" fill="none" stroke="var(--gold)" stroke-width="2">
  <rect x="2" y="5" width="32" height="44" rx="2"/><rect x="11" y="1" width="14" height="7" rx="2"/>
  <path d="M8 18h8M8 26h8M20 18h8M20 24h8M8 34h20M8 40h16"/>
  <circle cx="38" cy="46" r="9" fill="#fff"/><path d="M34 46l3 3 6-6"/>
</svg>
<svg class="icon" style="left:686px;top:433px" width="40" height="48" viewBox="0 0 40 48" fill="none" stroke="var(--gold)" stroke-width="2">
  <path d="M20 2l17 6v14c0 12-8 20-17 24C11 42 3 34 3 22V8z"/><path d="M20 7l12 4v11c0 9-6 15-12 18-6-3-12-9-12-18V11z"/>
  <circle cx="20" cy="22" r="7"/><path d="M17 22l2 2 4-4"/>
</svg>

<div class="principle-name" style="right:688px;top:167px"><span class="bracket">[</span>&nbsp; INTEGRITY <span class="bracket">]</span></div>
<p class="principle-text" style="right:688px;top:287px">Maintaining the highest standards<br>of quality.</p>

<div class="principle-name" style="right:382px;top:167px"><span class="bracket">[</span>&nbsp; ACCOUNTABILITY <span class="bracket">]</span></div>
<p class="principle-text" style="right:390px;top:287px">Providing service to our clients<br>which meets their exe\pectations</p>

<div class="principle-name" style="right:80px;top:167px"><span class="bracket">[</span>&nbsp; RELIABILITY <span class="bracket">]</span></div>
<p class="principle-text" style="right:83px;top:307px">Fullfilling the needs of our clients</p>

<div class="principle-name" style="right:688px;top:448px"><span class="bracket">[</span>&nbsp; ADAPTABILITY <span class="bracket">]</span></div>
<p class="principle-text" style="right:688px;top:526px">Preparing our activities to respond<br>to the demands of the present<br>Southern African and regional<br>Environment.</p>

<div class="principle-name" style="right:382px;top:448px"><span class="bracket">[</span>&nbsp; CAPABILITY <span class="bracket">]</span></div>
<p class="principle-text" style="right:390px;top:512px">Providing service to Affording our<br>staff, personal growth through<br>continuing education and/or<br>training. our clients which meets<br>their exe\pectations</p>

<div class="principle-name" style="right:80px;top:448px"><span class="bracket">[</span>&nbsp; ETHICS <span class="bracket">]</span></div>
<p class="principle-text" style="right:83px;top:492px">Providing equal opportunity to all, in<br>line with Government Policies.<br>Exercising zero tolerance to<br>discrimination in terms of Creed,<br>Politics, Religion, Disability, Gender<br>and Race</p>

<h2 class="section-title" style="left:402px;top:723px">CERTIFICATES</h2>

<div class="band">
  <p style="top:28px"><span class="bracket" style="font-size:15px">[</span>&nbsp; SATISFYING OUR CLIENTS THROUGH</p>
  <p style="top:55px">SERVICE EXELLENCE &nbsp;&nbsp;<span class="bracket" style="font-size:15px">]</span></p>
</div>

<svg class="abs" style="left:450px;top:822px" width="470" height="104" viewBox="0 0 470 104" role="img" aria-label="Certification badges">
  <circle cx="51" cy="50" r="49" fill="var(--badge-blue)" stroke="#9aa3d6" stroke-width="3"/>
  <rect x="148" y="14" width="160" height="66" rx="4" fill="var(--badge-red)" opacity=".85"/>
  <circle cx="405" cy="51" r="50" fill="var(--badge-sky)"/>
</svg>

<footer class="footer">
  <h3 style="left:134px"><span class="bracket">[</span>&nbsp; HEAD OFFICE <span class="bracket">]</span></h3>
  <address style="left:136px">P.O Box 410, Fernridge, 1640 7<br>Acacia Lane, Kestrel Park,<br>Midrand, 1692</address>

  <h3 style="left:416px"><span class="bracket">[</span>&nbsp; FREE STATE OFFICE <span class="bracket">]</span></h3>
  <address style="left:417px">Unit 9, Rosewood Centre<br>Bloemfontein 9300</address>

  <h3 style="left:697px"><span class="bracket">[</span>&nbsp; CONTACTS <span class="bracket">]</span></h3>
  <address style="left:696px">
    <div class="contact-row"><svg width="12" height="14" viewBox="0 0 12 14" fill="none" stroke="#bbb" stroke-width="1.4"><rect x="3" y="1" width="6" height="12" rx="1"/></svg>+27 (0) 87 555 0142 F</div>
    <div class="contact-row"><svg width="12" height="14" viewBox="0 0 12 14" fill="none" stroke="#bbb" stroke-width="1.4"><rect x="1" y="5" width="10" height="8"/><rect x="3" y="1" width="6" height="4"/></svg>086 555 0187</div>
    <div class="contact-row"><svg width="14" height="14" viewBox="0 0 14 14" fill="none" stroke="#bbb" stroke-width="1.4"><rect x="1" y="3" width="12" height="8"/><path d="M1 3l6 5 6-5"/></svg>info@brackenhaul.co.za</div>
  </address>
</footer>

</body>
</html>
```